Wireless Communication Company

We need a new web page for our company called Q3 Wavelinks based in Silicon Valley. We are a listed PMX company. We develop and supply a range of wireless communication devices to the machine to machine sector via cloud based technology. I have attached our logo which I would like to remain as per the photoshop colours (on the glossy sign).

Target Market(s)

Distributors or cloud based technology and communications devices

Industry/Entity Type

Communication

Number of Pages Required

5+ page

Font styles to use
Serif
Sans Serif

Colors
3176b5
0255a3
0492ce
34a7d8
85cae6
85abd2

Requirements
Must have
• A quality front page promoting our company. Looking very upmarket and tech savvy.
• Must be PMX compliant
Nice to have
• Update link to company announcements.

```html
<!DOCTYPE html>
<html lang="en">
<head>
<meta charset="utf-8">
<title>Q3 Wavelinks</title>
<link href="https://fonts.googleapis.com/css2?family=Open+Sans:wght@400;600;700&display=swap" rel="stylesheet">
<style>
:root{
  --navy:#16222d;
  --navy-2:#1f2f3d;
  --bar:#26394a;
  --blue:#0255a3;
  --blue-2:#3176b5;
  --sky:#0492ce;
  --sky-2:#34a7d8;
  --pale:#85cae6;
  --steel:#85abd2;
  --page:#e4e8eb;
  --band:#d3d8dc;
  --ink:#2a333b;
  --muted:#6b757e;
  --white:#ffffff;
}
*{box-sizing:border-box;margin:0;padding:0}
html,body{width:841px;height:1200px;overflow:hidden}
body{font-family:"Open Sans",Arial,sans-serif;background:var(--page);color:var(--ink);position:relative}
.wrap{position:absolute;left:135px;width:580px}

.site-header{position:absolute;top:0;left:0;width:841px;height:128px;background:radial-gradient(ellipse at 50% 30%,#2a3d4f 0%,var(--navy) 70%)}
.brand{position:absolute;left:0;right:0;top:54px;display:flex;justify-content:center;align-items:center;gap:8px}
.brand-dot{width:10px;height:10px;border-radius:50%;background:var(--steel)}
.brand-name{font-size:16px;font-weight:600;color:var(--steel);letter-spacing:.5px}

.main-nav{position:absolute;top:128px;left:0;width:841px;height:24px;background:var(--bar);border-top:1px solid #33495c}
.main-nav ul{position:absolute;left:135px;top:0;list-style:none;display:flex;height:24px}
.main-nav li{font-size:8px;font-weight:600;color:#c9d6e0;padding:0 9px;line-height:24px}
.main-nav li.active{background:var(--sky-2);color:var(--white)}

.hero{top:160px;height:322px;background:linear-gradient(135deg,#0c1824 0%,#17324a 45%,#0d1e2d 100%);overflow:hidden}
.hero-art{position:absolute;left:0;top:0;width:330px;height:322px;background:radial-gradient(circle at 55% 40%,#3d6f93 0%,#1b3850 45%,#0c1824 85%)}
.hero-copy{position:absolute;left:352px;top:86px;width:210px;color:var(--white)}
.hero-copy h1{font-size:20px;font-weight:400;line-height:1.25;margin-bottom:12px}
.hero-copy p{font-size:7.5px;line-height:1.5;color:#c7d4de}
.dots{position:absolute;right:16px;bottom:14px;display:flex;gap:4px}
.dots span{width:6px;height:6px;border-radius:50%;background:#6a8aa4}
.dots span.on{background:var(--white)}

.features{top:505px;height:120px;display:flex;gap:20px}
.card{flex:1;background:var(--white);border:1px solid #cfd5da;position:relative;padding:20px 12px 0}
.card-tab{position:absolute;top:-8px;left:50%;transform:translateX(-50%);background:var(--navy-2);color:var(--white);font-size:7.5px;font-weight:700;padding:4px 20px}
.card-tab.sky{background:var(--sky)}
.card h3{font-size:8px;font-weight:700;margin-bottom:4px;display:flex;align-items:center;gap:5px}
.card h3::before{content:"";width:7px;height:7px;border-radius:50%;background:var(--sky-2)}
.card p{font-size:6.5px;line-height:1.5;color:var(--muted)}
.read-more{position:absolute;right:10px;bottom:10px;font-size:6.5px;color:var(--white);background:var(--blue-2);padding:3px 8px}

.disrupt{position:absolute;top:648px;left:0;width:841px;height:182px;background:var(--band)}
.consult-art{position:absolute;left:135px;top:0;width:285px;height:182px;background:linear-gradient(180deg,#3b4650 0%,#5b6670 60%,#8b8f73 100%)}
.disrupt-copy{position:absolute;left:435px;top:26px;width:280px}
.disrupt-copy h2{font-size:14px;font-weight:600;line-height:1.3;margin-bottom:10px}
.disrupt-copy p{font-size:7px;line-height:1.55;color:var(--muted)}
.disrupt-copy .more{display:block;text-align:right;font-size:7px;color:var(--blue-2);margin-top:8px}

.lower{top:846px;height:262px;display:flex;gap:20px}
.col{flex:1;background:var(--white);border:1px solid #cfd5da}
.col-head{background:var(--navy-2);color:var(--white);font-size:8px;font-weight:700;text-align:center;padding:6px 0}
.col-head.sky{background:var(--sky)}
.quote{display:flex;gap:10px;padding:14px 12px 6px}
.avatar{width:50px;height:56px;flex:none;background:linear-gradient(180deg,#b9bfc4,#7d858c)}
.quote svg{flex:none;margin-top:2px}
.quote p{font-size:7px;line-height:1.5;color:var(--muted)}
.quote cite{display:block;font-style:normal;font-size:6.5px;color:var(--blue-2);margin-top:4px}
.partners{display:grid;grid-template-columns:repeat(3,1fr);gap:14px 16px;padding:20px 22px}
.partner{height:34px;background:#dfe4e8;border-radius:3px}
.partner.round{border-radius:50%;width:34px;justify-self:center}

.site-footer{position:absolute;top:1118px;left:0;width:841px;height:82px;background:var(--navy)}
.footer-inner{position:absolute;left:135px;top:10px;width:580px;display:flex;gap:22px}
.f-col{width:110px}
.f-col h4{font-size:6.5px;font-weight:700;color:var(--pale);margin-bottom:5px;text-transform:uppercase}
.f-col ul{list-style:none;columns:2}
.f-col li,.f-col p{font-size:6px;color:#9aa8b4;line-height:1.6}
.map{width:150px;height:62px;margin-left:auto;background:linear-gradient(135deg,#dfe3d6,#c9d3d9)}
</style>
</head>
<body>

<header class="site-header">
  <div class="brand">
    <span class="brand-dot"></span>
    <span class="brand-name">Q3 Wavelinks</span>
  </div>
</header>

<nav class="main-nav">
  <ul>
    <li class="active">HOME</li>
    <li>ABOUT US</li>
    <li>SERVICES</li>
    <li>PARTNERS</li>
    <li>CONTACT US</li>
  </ul>
</nav>

<section class="wrap hero">
  <div class="hero-art" role="img" aria-label="Glowing cloud above a circuit board landscape"></div>
  <div class="hero-copy">
    <h1>The World of Cloud Computing All in One Place!</h1>
    <p>Cloud computing is now being embraced by a majority of enterprises of all sizes. Yesterday's debate about public vs. private has transformed into the reality of hybrid cloud.</p>
  </div>
  <div class="dots"><span class="on"></span><span></span><span></span></div>
</section>

<section class="wrap features">
  <article class="card">
    <span class="card-tab">ABOUT US</span>
    <h3>Cloud computing driving</h3>
    <p>Our devices link machines to the cloud with secure wireless modules, giving partners fast, reliable data from every site they manage, day and night.</p>
    <span class="read-more">Read More »</span>
  </article>
  <article class="card">
    <span class="card-tab">SERVICES</span>
    <h3>Cloud computing driving</h3>
    <p>We design, supply and support machine to machine hardware with hosted platforms, so distributors can deploy connected products quickly and at scale.</p>
    <span class="read-more">Read More »</span>
  </article>
  <article class="card">
    <span class="card-tab sky">CLOUDAPPS</span>
    <h3>Cloud computing driving</h3>
    <p>Our cloud apps collect, store and present device data in clear dashboards, with alerts and reports that help teams act on real time insight.</p>
    <span class="read-more">Read More »</span>
  </article>
</section>

<section class="disrupt">
  <div class="consult-art" role="img" aria-label="Consulting illustration with a rocket launching into a cloud"></div>
  <div class="disrupt-copy">
    <h2>Disruptive but Essential in a Cloud Computing Universe.</h2>
    <p>The wireless sector is changing fast as more machines connect to the cloud. We help distributors stay ahead with dependable devices, flexible hosted services and expert guidance. Our team works closely with partners from first design to full rollout, making every connected project simpler, safer and ready for future growth.</p>
    <span class="more">Read More »</span>
  </div>
</section>

<section class="wrap lower">
  <div class="col">
    <div class="col-head">TESTIMONIALS</div>
    <div class="quote">
      <div class="avatar" role="img" aria-label="Portrait photo of a client"></div>
      <svg width="10" height="10" viewBox="0 0 10 10"><path d="M0 10V5L3 0h2L3 5h2v5zM5 10V5L8 0h2L8 5h2v5z" fill="#85abd2"/></svg>
      <p>I was impressed by the speed and care the team showed at every step. Our new devices went live on time and have worked perfectly since launch.<cite>— Dana Holt</cite></p>
    </div>
    <div class="quote">
      <div class="avatar" role="img" aria-label="Portrait photo of a client"></div>
      <svg width="10" height="10" viewBox="0 0 10 10"><path d="M0 10V5L3 0h2L3 5h2v5zM5 10V5L8 0h2L8 5h2v5z" fill="#85abd2"/></svg>
      <p>I have been very impressed with your friendliness and responsiveness. I would go so far as to say you set a benchmark for customer support.<cite>— Lee Marsh</cite></p>
    </div>
  </div>
  <div class="col">
    <div class="col-head sky">OUR PARTNERS</div>
    <div class="partners">
      <div class="partner"></div>
      <div class="partner"></div>
      <div class="partner round"></div>
      <div class="partner round"></div>
      <div class="partner"></div>
      <div class="partner"></div>
      <div class="partner"></div>
      <div class="partner round"></div>
      <div class="partner"></div>
      <div class="partner"></div>
      <div class="partner"></div>
      <div class="partner"></div>
    </div>
  </div>
</section>

<footer class="site-footer">
  <div class="footer-inner">
    <div class="f-col">
      <h4>Site Map</h4>
      <ul><li>Home</li><li>About</li><li>Services</li><li>Partners</li><li>News</li><li>Contact</li></ul>
    </div>
    <div class="f-col">
      <h4>Services</h4>
      <ul><li>Devices</li><li>Cloud</li><li>Support</li><li>Design</li><li>Hosting</li><li>Apps</li></ul>
    </div>
    <div class="f-col">
      <h4>Contact</h4>
      <p>100 Signal Way</p>
      <p>Silicon Valley, CA</p>
      <p>+1 555 0142</p>
    </div>
    <div class="map" role="img" aria-label="Location map of the office"></div>
  </div>
</footer>

</body>
</html>
```